BRAND BOOK design

We are a new swimwear brand. We have a vague idea of what we want. We have some colors we would like to use. We would love someone who can provide simple, sophisticated yet an edgy design for our first brand book. The brand book will contain our campaign photos and you will have to come up with layouts and simple designs to insert these photos and short quotes or descriptions. The brand book will contain our brand identity and express the vibes we want our customers to feel get from our brand.

Target Market(s)

US and Australia

Industry/Entity Type

Fashion

Font styles to use
Other font styles liked:
• Futura Medium

Colors
f9d9e8
cfcfcf
ffffff

Requirements
Must have
• simple modern layout with pop elements.
• photos must be placed with enough space.
• also need minimal space for words.
Nice to have
• Simple layouts that aren't common. Designs that can show our identity.
• Please refer to our website (under construction): www.brightkelphouse.com
Should not have
• mere copies of other brand designs

```html
<!DOCTYPE html>
<html lang="en">
<head>
<meta charset="utf-8">
<title>Brightkelp Brand Book Spreads</title>
<link href="https://fonts.googleapis.com/css2?family=Raleway:wght@200;300;400;500&display=swap" rel="stylesheet">
<style>
  :root{
    --bg:#80808f;
    --paper:#f4f4f4;
    --panel:#ececec;
    --white:#ffffff;
    --pink:#e8b6cc;
    --blush:#f9d9e8;
    --grey:#cfcfcf;
    --ink:#333333;
    --title:#c4c4c4;
    --gold:#d9a441;
    --sky:#b9d2e3;
    --sea:#9fbccb;
    --sand:#dccbb8;
    --sand-deep:#c9b39c;
  }
  *{box-sizing:border-box;margin:0;padding:0}
  html,body{width:1200px;height:1200px;overflow:hidden}
  body{background:var(--bg);font-family:"Raleway",sans-serif;color:var(--ink);position:relative}

  .spread{position:absolute;left:50px;width:1100px;height:420px;display:flex;box-shadow:0 16px 32px rgba(0,0,0,.28)}
  .spread--one{top:150px}
  .spread--two{top:640px}
  .page{position:relative;width:550px;height:420px;background:var(--paper);overflow:hidden}
  .page--left::after,.page--right::after{content:"";position:absolute;top:0;bottom:0;width:40px;pointer-events:none}
  .page--left::after{right:0;background:linear-gradient(90deg,rgba(0,0,0,0),rgba(0,0,0,.14))}
  .page--right::after{left:0;background:linear-gradient(90deg,rgba(0,0,0,.16),rgba(0,0,0,0))}

  .photo{position:absolute}
  .photo--beach-tower{background:
      linear-gradient(180deg,#dfe7ee 0%,#e6ebee 28%,#ece8e2 42%,#e6dbcf 70%,#d6c6b4 100%)}
  .photo--faded{background:
      radial-gradient(ellipse 70% 40% at 55% 60%,rgba(249,217,232,.85),rgba(249,217,232,0) 70%),
      linear-gradient(170deg,#f8e4ea 0%,#f4eef0 55%,#efeaec 100%)}
  .photo--shoreline{background:
      linear-gradient(180deg,#c8dce8 0%,#b9d0de 18%,#9fbccb 30%,#c9d4d6 40%,#e3ddd4 52%,#d9c9b6 78%,#c9b39c 100%)}
  .photo--palms{background:
      linear-gradient(180deg,#a8c6e0 0%,#b4cbdc 22%,#8fa892 32%,#b9c4c0 42%,#d9cbb8 58%,#d3bfa7 82%,#c6ae93 100%)}
  .photo--portrait{background:
      radial-gradient(ellipse 60% 30% at 50% 68%,rgba(240,190,214,.7),rgba(240,190,214,0) 70%),
      linear-gradient(180deg,#ece9ea 0%,#e8e2df 40%,#ead8de 70%,#e6d9d3 100%)}

  .product{position:absolute;font-size:9.5px;font-weight:400;line-height:1.3;letter-spacing:.3px;padding-left:18px;color:var(--ink)}
  .product::before{content:"";position:absolute;left:0;top:1px;width:11px;height:11px;border-radius:50%;background:var(--gold)}
  .product .price{margin-left:56px}

  .vertical-title{position:absolute;top:0;height:420px;width:60px;display:flex;align-items:center;justify-content:center}
  .vertical-title span{display:block;white-space:nowrap;font-weight:200;font-size:48px;letter-spacing:5px;color:var(--title)}
  .vertical-title--down span{transform:rotate(90deg)}
  .vertical-title--up span{transform:rotate(-90deg)}

  .block{position:absolute}
  .block--grey{background:var(--grey)}
  .block--pink{background:var(--pink)}
  .block--panel{background:var(--panel)}

  .headline{position:absolute;font-weight:200;font-size:42px;letter-spacing:4px;color:var(--title);white-space:nowrap}
  .rule{position:absolute;height:6px;background:var(--pink)}
  .copy{position:absolute;font-size:9.5px;line-height:1.4;width:240px;color:var(--ink)}
  .copy p{margin-bottom:11px}
</style>
</head>
<body>

<section class="spread spread--one">
  <div class="page page--left">
    <div class="photo photo--faded" role="img" aria-label="Faded pink swimsuit close-up with silver glitter star motifs" style="left:0;top:0;width:300px;height:420px"></div>
    <div class="product" style="left:70px;top:80px">
      ART. 45897 BIKINI BOTTOMS<br>92% Polyamid + 8% Elastan<br>new Collection 2018<br>PRICE<span class="price">€ 20.00</span>
    </div>
    <div class="photo photo--beach-tower" role="img" aria-label="Model in white strappy bikini on the beach by a lifeguard tower" style="left:300px;top:0;width:190px;height:420px"></div>
    <div class="vertical-title vertical-title--down" style="left:490px"><span>BRIGHTKELP</span></div>
  </div>
  <div class="page page--right">
    <div class="vertical-title vertical-title--up" style="left:0"><span>BRIGHTKELP</span></div>
    <div class="photo photo--shoreline" role="img" aria-label="Model in white open-back swimsuit and headscarf at the shoreline" style="left:60px;top:0;width:270px;height:420px"></div>
    <div class="product" style="left:345px;top:24px">
      ART. 45897 BIKINI BOTTOMS<br>92% Polyamid + 8% Elastan<br>new Collection 2018<br>PRICE<span class="price">€ 20.00</span>
    </div>
    <div class="block block--grey" style="left:330px;top:115px;width:50px;height:28px"></div>
    <div class="block block--pink" style="left:380px;top:143px;width:80px;height:277px"></div>
  </div>
</section>

<section class="spread spread--two">
  <div class="page page--left">
    <div class="product" style="left:60px;top:40px">
      ART. 45897 BIKINI BOTTOMS<br>92% Polyamid + 8% Elastan<br>new Collection 2018<br>PRICE<span class="price">€ 20.00</span>
    </div>
    <div class="block block--grey" style="left:220px;top:140px;width:60px;height:30px"></div>
    <div class="block block--pink" style="left:220px;top:170px;width:60px;height:250px"></div>
    <div class="photo photo--palms" role="img" aria-label="Model in pale blue swimsuit, cap and track pants kneeling on sand under palm trees" style="left:250px;top:40px;width:240px;height:380px"></div>
    <div class="vertical-title vertical-title--down" style="left:490px"><span>BRIGHTKELP</span></div>
  </div>
  <div class="page page--right">
    <div class="photo photo--portrait" role="img" aria-label="Faded portrait of model in pink lace-up bikini top with towel on head" style="left:0;top:0;width:260px;height:420px"></div>
    <div class="block block--panel" style="left:260px;top:0;width:290px;height:330px"></div>
    <div class="headline" style="left:190px;top:16px">BRIGHTKELP</div>
    <div class="rule" style="left:260px;top:70px;width:290px"></div>
    <div class="copy" style="left:285px;top:98px">
      <p>Lorem ipsum dolor sit amet, omnium consulatu repudiandae cu his. Rebum hendrerit ullamcorper usu ad, eruditi imperdiet vis ad, cu fabellas partiendo pro.</p>
      <p>Lorem ipsum dolor sit amet, omnium consulatu repudiandae cu his. Rebum hendrerit ullamcorper usu ad, eruditi imperdiet vis ad, cu fabellas partiendo pro.</p>
      <p>Lorem ipsum dolor sit amet, omnium consulatu repudiandae cu his. Rebum hendrerit ullamcorper usu ad, eruditi imperdiet vis ad, cu fabellas partiendo pro.</p>
    </div>
    <div class="block block--pink" style="left:260px;top:330px;width:290px;height:90px"></div>
  </div>
</section>

</body>
</html>
```